One page website for a Personal Injury Law Firm

Design and code a one page website in WordPress for the Brightwell Law Firm, which is a a personal injury law firm located in Coral Gables, Florida. Please note: if you want to change the color pallete for the logo and for the web design , that is fine by me.

Target Market(s)

Those injured in accidents that need legal representation

Industry/Entity Type

Legal

Coding

Coded - Design and coding required

Number of Pages Required

1 page

Font styles to use
Other font styles liked:
• Montserrat

```html
<!DOCTYPE html>
<html lang="en">
<head>
<meta charset="utf-8">
<title>Brightwell Law Firm — Personal Injury Representation</title>
<link href="https://fonts.googleapis.com/css2?family=DM+Serif+Display&family=Montserrat:wght@400;500;600;700&display=swap" rel="stylesheet">
<style>
:root{
  --navy:#24304f;
  --tan:#c9975f;
  --tan-soft:#d4a774;
  --ink:#222222;
  --body:#3d3d3d;
  --dark:#2b2b2b;
  --footer:#2e2e2e;
  --cream:#faf6f1;
  --white:#ffffff;
}
*{margin:0;padding:0;box-sizing:border-box}
html,body{width:1200px;height:5277px;overflow:hidden;background:var(--white)}
body{font-family:'Montserrat',sans-serif;color:var(--body);position:relative}
.serif{font-family:'DM Serif Display',serif;font-weight:400}
section,header,nav,footer{position:absolute;left:0;width:1200px}
.abs{position:absolute}
.h2{font-family:'DM Serif Display',serif;font-size:35px;color:var(--ink);line-height:1.1}
.sub{font-size:12px;font-weight:600;color:var(--ink)}
.txt{font-size:12px;line-height:21.5px;color:var(--body)}
.btn{position:absolute;display:flex;align-items:center;justify-content:center;font-size:12px;font-weight:600;text-transform:uppercase;color:var(--white);background:var(--tan-soft);border:2px solid #e6c59f;letter-spacing:.4px}

/* header */
.site-header{top:0;height:96px;background:var(--white)}
.brand{left:141px;top:28px;font-family:'DM Serif Display',serif;font-size:25px;color:var(--navy)}
.rating{left:500px;top:30px;display:flex;align-items:center;gap:8px}
.rating .dot{width:22px;height:22px;border-radius:50%;background:#d9d9d9}
.rating b{font-size:14px;color:var(--ink)}
.rating .stars{color:#e8a93a;font-size:10px;margin-left:4px}
.rating small{display:block;font-size:8px;color:#666}
.call{left:686px;top:30px;display:flex;align-items:center;gap:12px}
.call small{display:block;font-size:8px;color:#666}
.call b{font-size:13px;font-weight:600;color:var(--ink)}
.header-btn{left:862px;top:29px;width:195px;height:37px;border:2px solid var(--navy);display:flex;align-items:center;justify-content:center;font-family:'DM Serif Display',serif;font-size:15px;color:var(--navy)}

/* nav */
.main-nav{top:96px;height:41px;background:var(--tan)}
.main-nav span{position:absolute;top:13px;font-size:12px;color:var(--white);transform:translateX(-50%)}
.main-nav .active{border-bottom:1px solid var(--white);padding-bottom:5px}
.main-nav i{position:absolute;top:14px;width:1px;height:14px;background:rgba(255,255,255,.5)}

/* hero */
.hero{top:137px;height:527px;background:var(--navy)}
.hero-photo{left:600px;top:0;width:600px;height:527px;background:linear-gradient(120deg,#e9e7e3 0%,#b9b4ad 40%,#3a3a3e 70%,#1f2433 100%)}
.scroll-line{left:55px;top:70px;width:1px;height:210px;background:rgba(255,255,255,.6)}
.scroll-text{left:20px;top:340px;font-size:11px;letter-spacing:2px;color:var(--white);transform:rotate(-90deg);transform-origin:center;width:72px;text-align:center}
.scroll-dot{left:40px;top:423px;width:30px;height:30px;border-radius:50%;background:var(--white);display:flex;align-items:center;justify-content:center}
.hero h1{left:141px;top:104px;font-size:45px;font-weight:500;line-height:59px;color:var(--white);width:440px}
.hero .btn{left:141px;top:373px;width:211px;height:36px;border:none;background:var(--tan);text-transform:none;font-size:13px}

/* about */
.about{top:664px;height:661px}
.about-band{left:0;top:397px;width:506px;height:264px;background:var(--tan-soft)}
.about-frame{left:370px;top:94px;width:222px;height:180px;background:#2d2d2d}
.about-photo{left:141px;top:102px;width:439px;height:430px;background:linear-gradient(135deg,#6b5a4a,#c9b8a6 45%,#f2ece4 70%,#8c8478)}
.call-now{left:141px;top:566px;display:flex;align-items:center;gap:14px}
.call-now .ic{width:50px;height:50px;border-radius:50%;background:var(--white);display:flex;align-items:center;justify-content:center}
.call-now small{display:block;font-size:10px;font-weight:600;color:var(--white);letter-spacing:.5px}
.call-now b{font-size:25px;font-weight:600;color:var(--white)}
.call-rule{left:436px;top:603px;width:70px;height:1px;background:var(--white)}
.about-copy{left:660px;top:130px;width:400px}

/* why */
.why{top:1325px;height:883px;background:repeating-linear-gradient(120deg,#2d2d2d 0,#2d2d2d 80px,#272727 80px,#272727 160px)}
.center{text-align:center;width:1200px;left:0}
.why .h2{color:var(--white)}
.feature{width:300px;text-align:center}
.feature h3{font-family:'DM Serif Display',serif;font-weight:400;font-size:19px;line-height:24px;color:var(--white);margin:20px 0 10px}
.feature p{font-size:12px;line-height:18.5px;color:#e4e4e4}
.stories{left:170px;top:612px;width:860px;text-align:center;font-size:12px;line-height:22px;color:#e4e4e4}
.stories p{margin-bottom:14px}

/* strategy */
.strategy{top:2208px;height:665px}
.list-item{display:flex;gap:10px}
.tick{flex:none;width:14px;height:14px;border-radius:50%;background:var(--tan-soft);display:flex;align-items:center;justify-content:center;margin-top:2px}
.list-item h4{font-size:12px;font-weight:600;color:var(--ink);margin-bottom:6px}
.strategy-band{left:631px;top:311px;width:428px;height:262px;background:var(--tan-soft)}
.strategy-photo{left:653px;top:92px;width:383px;height:459px;background:linear-gradient(160deg,#eef2f4,#b9c6cf 45%,#39465a 75%,#27303e)}

/* practice */
.practice{top:2873px;height:664px;background:linear-gradient(100deg,#0e0e10 0%,#1d1f24 35%,#3e3f44 60%,#6a6b6f 80%,#2f3034 100%)}
.practice .h2{color:var(--white)}
.tile{position:absolute;background:rgba(40,40,42,.9);display:flex;align-items:center;justify-content:space-between;padding:0 20px;color:var(--white);font-family:'DM Serif Display',serif;font-size:14px;line-height:17px}
.tile.feature-tile{background:var(--tan-soft);display:block;padding:20px}
.feature-tile h3{font-family:'DM Serif Display',serif;font-weight:400;font-size:18px;margin-bottom:24px}
.feature-tile p{font-family:'Montserrat',sans-serif;font-size:11.5px;line-height:20px}

/* florida */
.florida{top:3537px;height:719px}
.florida-band{left:119px;top:242px;width:307px;height:387px;background:var(--tan-soft)}
.florida-photo{left:141px;top:94px;width:410px;height:514px;background:linear-gradient(150deg,#d4d9e2,#6f87a8 45%,#26415f 75%,#0e1f36)}

/* cta */
.cta{top:4256px;height:665px;background:var(--cream)}
.cta-box{left:141px;top:317px;width:918px;height:252px;border:2px solid var(--tan-soft)}
.cta-row{position:absolute;left:0;width:918px;display:flex;justify-content:center;align-items:center;gap:70px}
.cta-item{display:flex;align-items:center;gap:14px;font-family:'DM Serif Display',serif;font-size:16px;color:var(--ink)}
.cta-item span.plain{font-family:'Montserrat',sans-serif;font-size:14px}

/* footer */
.site-footer{top:4921px;height:356px;background:var(--footer);color:var(--white)}
.foot-brand{top:48px;font-family:'DM Serif Display',serif;font-size:30px}
.foot-nav span{position:absolute;top:126px;font-size:12px;font-weight:500;transform:translateX(-50%);letter-spacing:.3px}
.foot-nav i{position:absolute;top:127px;width:1px;height:12px;background:rgba(255,255,255,.5)}
.contact-item{position:absolute;top:206px;display:flex;gap:16px;align-items:flex-start}
.contact-item .ic{width:34px;height:34px;border-radius:50%;background:#e9e9e9;display:flex;align-items:center;justify-content:center;flex:none}
.contact-item p{font-size:12.5px;line-height:18px}
.foot-rule{left:141px;top:281px;width:918px;height:1px;background:rgba(255,255,255,.2)}
.copy{left:145px;top:313px;font-size:11px}
.social{position:absolute;top:306px;width:28px;height:28px;border-radius:50%;border:1px solid rgba(255,255,255,.7)}
</style>
</head>
<body>

<header class="site-header">
  <div class="abs brand">Brightwell Law Firm</div>
  <div class="abs rating">
    <span class="dot"></span>
    <div><b>500+</b><span class="stars">★★★★★</span><small>Five Star Client Reviews</small></div>
  </div>
  <div class="abs call">
    <svg width="22" height="22" viewBox="0 0 24 24" fill="none" stroke="#c9975f" stroke-width="2"><path d="M5 3h4l2 5-2.5 1.5a11 11 0 0 0 6 6L16 13l5 2v4a2 2 0 0 1-2 2A16 16 0 0 1 3 5a2 2 0 0 1 2-2z"/></svg>
    <div><small>Call or Text 24/7</small><b>123-456-7890</b></div>
  </div>
  <div class="abs header-btn">Schedule A Free Call</div>
</header>

<nav class="main-nav">
  <span class="active" style="left:160px">Home</span><i style="left:230px"></i>
  <span style="left:315px">About Us</span><i style="left:400px"></i>
  <span style="left:496px">Practice Areas</span><i style="left:594px"></i>
  <span style="left:694px">Why Choose Us</span><i style="left:790px"></i>
  <span style="left:866px">Blogs</span><i style="left:945px"></i>
  <span style="left:1024px">Contact Us</span>
</nav>

<section class="hero">
  <div class="abs scroll-line"></div>
  <div class="abs scroll-text">SCROLL DOWN</div>
  <div class="abs scroll-dot"><svg width="12" height="12" viewBox="0 0 12 12" fill="none" stroke="#24304f" stroke-width="1.6"><path d="M3 5l3 3 3-3"/></svg></div>
  <h1 class="abs">Concierge-Level Personal Injury Representation In Miami, Florida</h1>
  <div class="btn">Schedule A Free Call</div>
  <div class="abs hero-photo" role="img" aria-label="Photo of clasped hands at a desk beside a gavel, book and scales of justice"></div>
</section>

<section class="about">
  <div class="abs about-band"></div>
  <div class="abs about-frame"></div>
  <div class="abs about-photo" role="img" aria-label="Photo of a client and lawyer signing a document"></div>
  <div class="abs call-now">
    <div class="ic"><svg width="22" height="22" viewBox="0 0 24 24" fill="none" stroke="#c9975f" stroke-width="2"><path d="M5 3h4l2 5-2.5 1.5a11 11 0 0 0 6 6L16 13l5 2v4a2 2 0 0 1-2 2A16 16 0 0 1 3 5a2 2 0 0 1 2-2z"/></svg></div>
    <div><small>CALL US NOW</small><b>(123) 456 7890</b></div>
  </div>
  <div class="abs call-rule"></div>
  <div class="abs about-copy">
    <h2 class="h2">The Brightwell Law Firm</h2>
    <p class="sub" style="margin:16px 0 10px">Justice. Recovery. A Better Future Starts Here.</p>
    <p class="txt">At The Brightwell Law Firm, we understand that suffering a personal injury can be life-altering-physically, emotionally, and financially. You may be unsure whether pursuing legal action is the right step. But in Florida, holding negligent parties accountable isn't just your right-it's often necessary to rebuild your life.</p>
    <p class="txt" style="margin-top:22px">We take a concierge-style approach to personal injury law, offering personalized attention, strategic advocacy, and relentless dedication to securing the maximum compensation you deserve. Our mission is not only to make you whole again but to help you build a brighter future-ensuring access to the best medical care, financial stability, and peace of mind for you and your loved one.</p>
  </div>
  <div class="btn" style="left:660px;top:556px;width:139px;height:43px">Read More</div>
</section>

<section class="why">
  <h2 class="abs center h2" style="top:122px">Why Choose The Brightwell Law Firm?</h2>
  <p class="abs center" style="top:181px;font-size:12px;color:#e4e4e4">Unmatched Experience. Proven Results. Relentless Advocacy.</p>
  <div class="abs feature" style="left:129px;top:240px">
    <svg width="144" height="160" viewBox="0 0 144 160" fill="none" stroke="#c9975f" stroke-width="6"><path d="M72 6l62 36v76l-62 36-62-36V42z"/><g stroke="#fff" stroke-width="3"><rect x="44" y="58" width="14" height="44"/><rect x="58" y="58" width="14" height="44"/><rect x="72" y="58" width="14" height="44"/><path d="M86 60l12-4 12 42-12 4z"/></g></svg>
    <h3>25+ Years of<br>Legal Mastery</h3>
    <p>We have successfully handled thousands of cases, fighting both for and against insurance companies. This unique dual experience gives us an insider advantage in every case we take on.</p>
  </div>
  <div class="abs feature" style="left:450px;top:240px">
    <svg width="144" height="160" viewBox="0 0 144 160" fill="none" stroke="#c9975f" stroke-width="6"><path d="M72 6l62 36v76l-62 36-62-36V42z"/><g stroke="#fff" stroke-width="3"><rect x="46" y="50" width="44" height="58" rx="3"/><path d="M54 66h10M54 80h10M54 94h10M70 66h12"/><path d="M82 80l14 6v10c0 8-6 12-14 14-8-2-14-6-14-14V86z"/></g></svg>
    <h3>Extensive Knowledge of<br>Insurance Tactics</h3>
    <p>Having worked for insurance companies, we know their strategies, loopholes, and how to dismantle their defenses to maximize your settlement.</p>
  </div>
  <div class="abs feature" style="left:770px;top:240px">
    <svg width="144" height="160" viewBox="0 0 144 160" fill="none" stroke="#c9975f" stroke-width="6"><path d="M72 6l62 36v76l-62 36-62-36V42z"/><g stroke="#fff" stroke-width="3"><circle cx="72" cy="80" r="26"/><circle cx="72" cy="80" r="16"/><path d="M76 72h-6a3 3 0 0 0 0 6h4a3 3 0 0 1 0 6h-6M72 68v24"/></g></svg>
    <h3>Millions Recovered<br>for Clients</h3>
    <p>Our track record includes life-changing results.</p>
  </div>
  <div class="abs stories">
    <p>A client fell eight feet at a major sporting venue and suffered catastrophic injuries. We recovered compensation that covered all medical bills, paid off their home, and funded their children's college education.</p>
    <p>A client suffered a severe infection from a minor slip-and-fall injury in a Miami condo building. We resolved the case before filing a lawsuit, securing funds that allowed him to buy a new home, pay off debts, and provide private school tuition for his children.</p>
    <p>A fast-food restaurant's napkin dispenser fell on a customer's face, breaking her nose and leaving her permanently disfigured. We secured a settlement that covered plastic surgery, home renovations, and her daughter's college tuition.</p>
    <p>These are just a few examples of how we fight for our clients' futures—not just their cases.</p>
  </div>
</section>

<section class="strategy">
  <h2 class="abs h2" style="left:141px;top:124px">Our Strategy</h2>
  <p class="abs sub" style="left:141px;top:178px">Aggressive, Client-Focused, and Results-Driven</p>
  <div class="abs" style="left:141px;top:212px;width:430px">
    <div class="list-item"><span class="tick"><svg width="8" height="8" viewBox="0 0 8 8" fill="none" stroke="#fff" stroke-width="1.6"><path d="M1 4l2 2 4-4"/></svg></span><div><h4>Taking on Corporate Giants</h4><p class="txt">We don't back down from big insurance companies, property management firms, or major corporations. We fight for justice-no matter how powerful the opposition.</p></div></div>
    <div class="list-item" style="margin-top:22px"><span class="tick"><svg width="8" height="8" viewBox="0 0 8 8" fill="none" stroke="#fff" stroke-width="1.6"><path d="M1 4l2 2 4-4"/></svg></span><div><h4>Concierge-Style Legal Care</h4><p class="txt">You're not just another case number. We provide dedicated, personalized service, keeping you informed, supported, and empowered throughout the legal process.</p></div></div>
    <div class="list-item" style="margin-top:22px"><span class="tick"><svg width="8" height="8" viewBox="0 0 8 8" fill="none" stroke="#fff" stroke-width="1.6"><path d="M1 4l2 2 4-4"/></svg></span><div><h4>No Win, No Fee Guarantee</h4><p class="txt">We take your case on a contingency basis, which means you pay nothing unless we win.</p></div></div>
  </div>
  <div class="btn" style="left:141px;top:530px;width:140px;height:43px">Contact Us</div>
  <div class="abs strategy-band"></div>
  <div class="abs strategy-photo" role="img" aria-label="Photo of two lawyers in suits talking in an office"></div>
</section>

<section class="practice" role="img" aria-label="Photo of a firefighter beside a damaged car at an accident scene">
  <h2 class="abs h2" style="left:141px;top:125px">Our Practice Areas</h2>
  <div class="tile feature-tile" style="left:141px;top:264px;width:219px;height:222px">
    <h3>Car Accidents</h3>
    <p>We fight for victims of rear-end crashes, multi-vehicle collisions, pedestrian and cyclist accidents, and more.</p>
  </div>
  <div class="tile" style="left:371px;top:414px;width:221px;height:72px">Slip and Fall /<br>Premises Liability<svg width="26" height="26" viewBox="0 0 24 24" fill="none" stroke="#fff" stroke-width="1.4"><circle cx="12" cy="5" r="2"/><path d="M12 8l-3 6h5l3 6M9 14l-4 4"/></svg></div>
  <div class="tile" style="left:602px;top:414px;width:221px;height:72px">Wrongful<br>Death<svg width="26" height="26" viewBox="0 0 24 24" fill="none" stroke="#fff" stroke-width="1.4"><path d="M7 21V9a5 5 0 0 1 10 0v12zM4 21h16"/></svg></div>
  <div class="tile" style="left:836px;top:414px;width:223px;height:72px">Product<br>Liability<svg width="26" height="26" viewBox="0 0 24 24" fill="none" stroke="#fff" stroke-width="1.4"><rect x="5" y="3" width="14" height="18" rx="2"/><path d="M9 8h6M9 12h6M9 16h4"/></svg></div>
  <div class="tile" style="left:141px;top:500px;width:219px;height:72px">Truck &amp; Commercial<br>Vehicle Accidents<svg width="26" height="26" viewBox="0 0 24 24" fill="none" stroke="#fff" stroke-width="1.4"><path d="M2 7h12v9H2zM14 10h4l3 3v3h-7z"/><circle cx="6" cy="18" r="1.5"/><circle cx="17" cy="18" r="1.5"/></svg></div>
  <div class="tile" style="left:371px;top:500px;width:221px;height:72px">Boating &amp; Watercraft<br>Accidents<svg width="26" height="26" viewBox="0 0 24 24" fill="none" stroke="#fff" stroke-width="1.4"><path d="M12 3v12M12 4l6 10h-6M3 17h18l-3 4H6z"/></svg></div>
  <div class="tile" style="left:602px;top:500px;width:221px;height:72px">Dog Bites and<br>Animal Attacks<svg width="26" height="26" viewBox="0 0 24 24" fill="none" stroke="#fff" stroke-width="1.4"><circle cx="6" cy="9" r="2"/><circle cx="10" cy="5" r="2"/><circle cx="14" cy="5" r="2"/><circle cx="18" cy="9" r="2"/><path d="M8 17c0-3 2-5 4-5s4 2 4 5-8 3-8 0z"/></svg></div>
  <div class="tile" style="left:836px;top:500px;width:223px;height:72px">Workplace<br>Injuries<svg width="26" height="26" viewBox="0 0 24 24" fill="none" stroke="#fff" stroke-width="1.4"><path d="M4 15a8 8 0 0 1 16 0zM2 15h20M12 7v4"/></svg></div>
</section>

<section class="florida">
  <div class="abs florida-band"></div>
  <div class="abs florida-photo" role="img" aria-label="Photo of a gavel with blue digital binary overlay"></div>
  <div class="abs" style="left:608px;top:124px;width:460px">
    <h2 class="h2">Florida Personal Injury Law</h2>
    <p class="sub" style="margin:16px 0 12px">Your Rights and Legal Protections</p>
    <div class="list-item"><span class="tick"><svg width="8" height="8" viewBox="0 0 8 8" fill="none" stroke="#fff" stroke-width="1.6"><path d="M1 4l2 2 4-4"/></svg></span><div><h4>Comparative Negligence (Florida Statutes §768.81)</h4><p class="txt">Even if you were partially at fault, you can still recover compensation. Your damages will be reduced based on your percentage of fault.</p></div></div>
    <div class="list-item" style="margin-top:22px"><span class="tick"><svg width="8" height="8" viewBox="0 0 8 8" fill="none" stroke="#fff" stroke-width="1.6"><path d="M1 4l2 2 4-4"/></svg></span><div><h4>Statute of Limitations (Florida Statutes §95.11)</h4><p class="txt">You have four years to file a personal injury claim and two years for wrongful death cases. Missing these deadlines can prevent you from recovering compensation.</p></div></div>
    <div class="list-item" style="margin-top:22px"><span class="tick"><svg width="8" height="8" viewBox="0 0 8 8" fill="none" stroke="#fff" stroke-width="1.6"><path d="M1 4l2 2 4-4"/></svg></span><div><h4>Premises Liability (Florida Statutes §768.0755)</h4><p class="txt">Property owners are responsible for dangerous conditions they knew or should have known about.</p></div></div>
  </div>
  <div class="btn" style="left:608px;top:528px;width:142px;height:47px">Contact Us</div>
</section>

<section class="cta">
  <h2 class="abs center h2" style="top:124px">Take the First Step Toward Justice</h2>
  <p class="abs center" style="top:184px;font-size:12px;color:var(--ink)">Let Us Fight for the Compensation You Deserve</p>
  <p class="abs center" style="top:214px;font-size:12px;color:var(--body)">If you have been injured due to someone else's negligence, do not wait. Time-sensitive deadlines could impact your case</p>
  <div class="abs cta-box">
    <div class="cta-row" style="top:10px">
      <div class="cta-item"><svg width="56" height="62" viewBox="0 0 56 62" fill="none" stroke="#d4a774" stroke-width="2"><path d="M28 2l25 14v30L28 60 3 46V16z"/><path d="M28 44s-9-9-9-15a9 9 0 0 1 18 0c0 6-9 15-9 15z"/><circle cx="28" cy="29" r="3"/></svg><span>Visit: <span class="plain">418 Palmetto Avenue, Coral Gables, FL 33134</span></span></div>
    </div>
    <div class="cta-row" style="top:94px;gap:34px">
      <div class="cta-item"><svg width="56" height="62" viewBox="0 0 56 62" fill="none" stroke="#d4a774" stroke-width="2"><path d="M28 2l25 14v30L28 60 3 46V16z"/><circle cx="28" cy="26" r="6"/><path d="M17 42a11 11 0 0 1 22 0"/></svg>Free Consultation</div>
      <div class="cta-item"><svg width="56" height="62" viewBox="0 0 56 62" fill="none" stroke="#d4a774" stroke-width="2"><path d="M28 2l25 14v30L28 60 3 46V16z"/><circle cx="28" cy="31" r="11"/><path d="M20 23l16 16"/></svg>No Fees Unless We Win</div>
      <div class="cta-item"><svg width="56" height="62" viewBox="0 0 56 62" fill="none" stroke="#d4a774" stroke-width="2"><path d="M28 2l25 14v30L28 60 3 46V16z"/><path d="M28 20l10 4v8c0 6-5 9-10 11-5-2-10-5-10-11v-8z"/></svg>Aggressive Representation</div>
    </div>
    <div class="cta-row" style="top:178px">
      <div class="cta-item"><svg width="56" height="62" viewBox="0 0 56 62" fill="none" stroke="#d4a774" stroke-width="2"><path d="M28 2l25 14v30L28 60 3 46V16z"/><path d="M20 40l12-12M26 22l10 10M18 44h14"/></svg><span>The Brightwell Law Firm: <span class="plain">Where Justice Meets Dedication.</span></span></div>
    </div>
  </div>
</section>

<footer class="site-footer">
  <div class="abs center foot-brand">Brightwell Law Firm</div>
  <div class="foot-nav">
    <span style="left:295px">HOME</span><i style="left:346px"></i>
    <span style="left:406px">ABOUT US</span><i style="left:470px"></i>
    <span style="left:555px">PRACTICE AREAS</span><i style="left:640px"></i>
    <span style="left:725px">WHY CHOOSE US</span><i style="left:810px"></i>
    <span style="left:881px">CONTACT US</span>
  </div>
  <div class="contact-item" style="left:183px">
    <span class="ic"><svg width="16" height="16" viewBox="0 0 24 24" fill="none" stroke="#2e2e2e" stroke-width="2"><rect x="3" y="5" width="18" height="14"/><path d="M3 6l9 7 9-7"/></svg></span>
    <p>Email<br>info@brightwelllawfirm.com</p>
  </div>
  <div class="contact-item" style="left:501px">
    <span class="ic"><svg width="16" height="16" viewBox="0 0 24 24" fill="none" stroke="#2e2e2e" stroke-width="2"><path d="M12 21s-7-7-7-12a7 7 0 0 1 14 0c0 5-7 12-7 12z"/><circle cx="12" cy="9" r="2.5"/></svg></span>
    <p>Address<br>418 Palmetto Avenue,<br>Coral Gables, FL 33134</p>
  </div>
  <div class="contact-item" style="left:798px">
    <span class="ic"><svg width="16" height="16" viewBox="0 0 24 24" fill="none" stroke="#2e2e2e" stroke-width="2"><path d="M5 3h4l2 5-2.5 1.5a11 11 0 0 0 6 6L16 13l5 2v4a2 2 0 0 1-2 2A16 16 0 0 1 3 5a2 2 0 0 1 2-2z"/></svg></span>
    <p>Phone<br>(123) 456 7890</p>
  </div>
  <div class="abs foot-rule"></div>
  <div class="abs copy">© 2025 The Brightwell Law Firm. All Rights Reserved.</div>
  <span class="social" style="left:918px"></span>
  <span class="social" style="left:955px"></span>
  <span class="social" style="left:992px"></span>
  <span class="social" style="left:1029px"></span>
</footer>

</body>
</html>
```